Experienced Handyman needs a business card design

Need a business card design for a one-person Handyman business. This will be my second job (part-time) after retiring from a hands-on 30-year career. I'm experienced, a hard worker, friendly, and do quality work. Everybody needs a handman they can rely on! I've worked with wood and home renovations for 20 years on the side. I'm interested in small, quick jobs - not big renovations, or building decks or garages - more like home maintenance, installing sinks, - things like that.
Walter The Fixer LLC
Small Jobs Done Right
I'm wondering if the P or H could be made out of tools in my logo...?
Target Market(s)
Homeowners - small jobs
Industry/Entity Type
Handyman / Construction
Contact Information for Business Card
Business name & tagline (see description)...email (Walter@WalterTheFixerpro.example)...phone (555) 417-8862
Look and feel

```html
<!DOCTYPE html>
<html lang="en">
<head>
<meta charset="utf-8">
<title>Walter The Fixer LLC — Business Card</title>
<link rel="stylesheet" href="https://fonts.googleapis.com/css2?family=Montserrat:wght@400;500;800&display=swap">
<style>
  :root {
    --backdrop: #d6d6d6;
    --brand-blue: #0b55b0;
    --card-white: #ffffff;
    --ink: #2b2b2b;
    --rule: #3a3a3a;
  }
  * { box-sizing: border-box; margin: 0; padding: 0; }
  html, body { width: 1200px; height: 913px; overflow: hidden; }
  body {
    background: var(--backdrop);
    font-family: "Montserrat", sans-serif;
    position: relative;
  }
  .card {
    position: absolute;
    top: 308px;
    width: 525px;
    height: 300px;
    box-shadow: 0 10px 28px rgba(0,0,0,0.22);
  }
  .card--front { left: 45px; background: var(--card-white); }
  .card--back { left: 630px; background: var(--brand-blue); }

  .brand { position: absolute; display: flex; align-items: center; gap: 12px; }
  .brand__mark { width: 34px; height: 34px; flex: none; }
  .brand__name {
    font-weight: 800;
    font-size: 22px;
    letter-spacing: 0.04em;
    text-transform: uppercase;
    line-height: 1;
  }
  .tagline {
    position: absolute;
    font-weight: 500;
    font-size: 10.5px;
    letter-spacing: 0.22em;
    text-transform: uppercase;
  }

  .card--front .brand { left: 70px; top: 60px; }
  .card--front .brand__mark { background: var(--brand-blue); }
  .card--front .brand__name { color: var(--brand-blue); }
  .card--front .tagline { left: 116px; top: 102px; color: var(--brand-blue); }

  .rule-long {
    position: absolute; left: 200px; right: 40px; top: 140px;
    height: 1px; background: var(--rule);
  }
  .person { position: absolute; left: 70px; top: 168px; }
  .person__name {
    font-weight: 800; font-size: 22px; color: var(--brand-blue);
    letter-spacing: 0.03em; text-transform: uppercase;
  }
  .person__role { font-weight: 400; font-size: 14px; color: var(--ink); margin-top: 2px; }
  .rule-short {
    position: absolute; left: 70px; width: 180px; top: 224px;
    height: 1px; background: var(--rule);
  }
  .contact { position: absolute; left: 70px; top: 236px; list-style: none; }
  .contact__item {
    display: flex; align-items: center; gap: 10px;
    font-size: 13.5px; color: var(--ink); line-height: 24px;
  }
  .contact__icon { width: 14px; height: 14px; flex: none; }

  .card--back .brand { left: 50%; top: 118px; transform: translateX(-50%); }
  .card--back .brand__mark { background: var(--card-white); }
  .card--back .brand__name { color: var(--card-white); font-size: 26px; white-space: nowrap; }
  .card--back .tagline {
    left: 0; right: 0; top: 166px; text-align: center;
    color: var(--card-white); font-size: 12px;
  }
</style>
</head>
<body>
  <section class="card card--front" aria-label="Business card front">
    <div class="brand">
      <span class="brand__mark"></span>
      <span class="brand__name">Walter The Fixer LLC</span>
    </div>
    <p class="tagline">Small Jobs Done Right</p>
    <div class="rule-long"></div>
    <div class="person">
      <p class="person__name">Walter</p>
      <p class="person__role">Managing Director</p>
    </div>
    <div class="rule-short"></div>
    <ul class="contact">
      <li class="contact__item">
        <svg class="contact__icon" viewBox="0 0 24 24" aria-hidden="true">
          <path fill="#0b55b0" d="M6.6 10.8a15.1 15.1 0 0 0 6.6 6.6l2.2-2.2a1 1 0 0 1 1-.25 11.4 11.4 0 0 0 3.6.57 1 1 0 0 1 1 1V20a1 1 0 0 1-1 1A17 17 0 0 1 3 4a1 1 0 0 1 1-1h3.5a1 1 0 0 1 1 1c0 1.25.2 2.45.57 3.57a1 1 0 0 1-.25 1z"/>
        </svg>
        (555) 417-8862
      </li>
      <li class="contact__item">
        <svg class="contact__icon" viewBox="0 0 24 24" aria-hidden="true">
          <rect x="2" y="5" width="20" height="14" fill="#0b55b0"/>
          <path d="M2 5l10 8 10-8" fill="none" stroke="#fff" stroke-width="1.6"/>
        </svg>
        Walter@WalterTheFixerpro.example
      </li>
    </ul>
  </section>

  <section class="card card--back" aria-label="Business card back">
    <div class="brand">
      <span class="brand__mark"></span>
      <span class="brand__name">Walter The Fixer LLC</span>
    </div>
    <p class="tagline">Small Jobs Done Right</p>
  </section>
</body>
</html>
```